Scheduled Servicing Forms

Quillmoor Systems requires two schedule servicing forms to be created on designer templates for our engineers to complete when servicing customers. We will complete these forms on a periodic basis, and send to the customer on completion of the work.
We have two forms that need to be created:
• Hybrid Cloud Customer Service
• Brindlecast Cloud Customer Service
Please do not reference our website for ideas as its about to change. “Specialised Consulting” is our new go to market, not “Charting the Frontiers of Computing. Our new website (still under development) is available at https://quillmoorsystems.dev-preview.example and will be officially launched shortly.
Our company theme is “Blue” and we want to keep a blue theme for the work.
Please ensure there is “Ample” space for engineers to write comments next to each audit item.
We have uploaded examples of the content that needs to be created for both form in Word and Excel format.
The designer must upload the source files (not just PDF) so we can edit the content on the forms at a later date.
The forms must be in standard A4 size (multiple pages).
Information Technology

```html
<!DOCTYPE html>
<html lang="en">
<head>
<meta charset="utf-8">
<title>Quillmoor Systems – Scheduled Service Checklist</title>
<link href="https://fonts.googleapis.com/css2?family=Andika:wght@400;700&display=swap" rel="stylesheet">
<style>
  :root{
    --backdrop:#ababab;
    --paper:#ffffff;
    --brand-blue:#1f7fcb;
    --brand-blue-dark:#1469b3;
    --rule:#2a7fc8;
    --ink:#2b2b2b;
    --line:#9a9a9a;
    --box:#8c8c8c;
    --tint:#eef4fa;
  }
  *{box-sizing:border-box;margin:0;padding:0}
  html,body{width:806px;height:1200px;overflow:hidden}
  body{background:var(--backdrop);font-family:"Andika",sans-serif;color:var(--ink);position:relative}
  .sheet{position:absolute;left:212px;width:382px;height:541px;background:var(--paper)}
  .sheet--one{top:49px}
  .sheet--two{top:616px;background:linear-gradient(160deg,var(--tint) 0%,var(--paper) 18%,var(--paper) 82%,var(--tint) 100%)}
  .masthead{height:67px;background:linear-gradient(180deg,var(--brand-blue) 0%,var(--brand-blue-dark) 100%);color:#fff;text-align:center;font-weight:700;font-size:10.5px;line-height:16px;padding-top:10px;letter-spacing:.2px}
  .job-meta{position:absolute;left:24px;top:76px;font-size:5.5px;line-height:11px}
  .job-meta .field{display:flex;align-items:flex-end;gap:4px}
  .job-meta .blank{display:inline-block;border-bottom:.6px solid var(--line);height:6px}
  .checklist{position:absolute;left:17px;width:349px;border:1px solid var(--rule)}
  .sheet--one .checklist{top:102px}
  .sheet--two .checklist{top:57px}
  .row{display:grid;grid-template-columns:175px 1fr;border-top:1px solid var(--rule)}
  .row:first-child{border-top:none}
  .row > div{padding:0 6px}
  .item{border-right:1px solid var(--rule);display:flex;align-items:center;font-size:5.4px;line-height:7.5px}
  .head{height:16px}
  .head div{font-weight:700;font-size:7px;display:flex;align-items:center}
  .sheet--one .row.std{height:26.6px}
  .sheet--two .row.std{height:28.2px}
  .row.score{height:92px}
  .result{font-size:5px;line-height:8px;padding-top:3px!important;display:flex;flex-direction:column;justify-content:center}
  .score .result{justify-content:flex-start;padding-top:7px!important}
  .choices{display:flex;gap:14px}
  .choices span{display:flex;align-items:center;gap:3px}
  .choices i{display:inline-block;width:5px;height:5px;border:.6px solid var(--box)}
  .answer{display:flex;align-items:flex-end;gap:3px}
  .answer b{font-weight:400}
  .answer .blank{flex:1;border-bottom:.6px solid var(--line);height:6px;margin-right:16px}
  .recs{padding-left:7px}
  .recs .answer .blank{margin-right:42px}
</style>
</head>
<body>

<section class="sheet sheet--one">
  <header class="masthead">Quillmoor Systems<br>Brindlecast Hybrid/On-Premise<br>Scheduled Service Checklist</header>
  <div class="job-meta">
    <div class="field">Customer: <span class="blank" style="width:215px"></span></div>
    <div class="field">Date: <span class="blank" style="width:14px"></span><span class="blank" style="width:14px"></span><span class="blank" style="width:14px"></span></div>
  </div>
  <div class="checklist">
    <div class="row head"><div class="item">Maintenance Check</div><div>Result</div></div>
    <div class="row std"><div class="item">Active backup for all B365 accounts (manual check) - ensuring all items are included in the job</div><div class="result"><div class="choices"><span><i></i>Yes</span><span><i></i>No</span></div><div class="answer"><b>Comment:</b><span class="blank"></span></div></div></div>
    <div class="row std"><div class="item">Test restore from server backup</div><div class="result"><div class="choices"><span><i></i>Yes</span><span><i></i>No</span></div><div class="answer"><b>Comment:</b><span class="blank"></span></div></div></div>
    <div class="row std"><div class="item">Test restore of an email</div><div class="result"><div class="choices"><span><i></i>Yes</span><span><i></i>No</span></div><div class="answer"><b>Comment:</b><span class="blank"></span></div></div></div>
    <div class="row std"><div class="item">Test restore of ShareVault file</div><div class="result"><div class="choices"><span><i></i>Yes</span><span><i></i>No</span></div><div class="answer"><b>Comment:</b><span class="blank"></span></div></div></div>
    <div class="row std"><div class="item">Log into Antivirus products (ensure all endpoint devices have active antivirus and are up to date)</div><div class="result"><div class="choices"><span><i></i>Yes</span><span><i></i>No</span></div><div class="answer"><b>Comment:</b><span class="blank"></span></div></div></div>
    <div class="row std"><div class="item">Check Spam filters</div><div class="result"><div class="choices"><span><i></i>Yes</span><span><i></i>No</span></div><div class="answer"><b>Comment:</b><span class="blank"></span></div></div></div>
    <div class="row std"><div class="item">Check that all users have MFA enabled</div><div class="result"><div class="choices"><span><i></i>Yes</span><span><i></i>No</span></div><div class="answer"><b>Comment:</b><span class="blank"></span></div></div></div>
    <div class="row std"><div class="item">Review B365 Risk Detections</div><div class="result"><div class="choices"><span><i></i>Yes</span><span><i></i>No</span></div><div class="answer"><b>Comment:</b><span class="blank"></span></div></div></div>
    <div class="row std"><div class="item">Confirm Audit Log enabled</div><div class="result"><div class="choices"><span><i></i>Yes</span><span><i></i>No</span></div><div class="answer"><b>Comment:</b><span class="blank"></span></div></div></div>
    <div class="row std"><div class="item">Review B365 license expiry dates</div><div class="result"><div class="choices"><span><i></i>Yes</span><span><i></i>No</span></div><div class="answer"><b>Comment:</b><span class="blank"></span></div></div></div>
    <div class="row std"><div class="item">Review external sharing in ShareVault/DriveSync</div><div class="result"><div class="choices"><span><i></i>Yes</span><span><i></i>No</span></div><div class="answer"><b>Comment:</b><span class="blank"></span></div></div></div>
    <div class="row std"><div class="item">Check Compliance status</div><div class="result"><div class="choices"><span><i></i>Yes</span><span><i></i>No</span></div><div class="answer"><b>Comment:</b><span class="blank"></span></div></div></div>
    <div class="row score"><div class="item" style="align-items:flex-start;padding-top:6px">Check and record Brindlecast security score</div>
      <div class="result">
        <div class="choices"><span><i></i>Yes</span><span><i></i>No</span></div>
        <div class="answer"><b>Score:</b><span class="blank" style="margin-right:32px"></span></div>
        <div>Top 5 Recommendations:</div>
        <div class="recs">
          <div class="answer"><b>1:</b><span class="blank"></span></div>
          <div class="answer"><b>2:</b><span class="blank"></span></div>
          <div class="answer"><b>3:</b><span class="blank"></span></div>
          <div class="answer"><b>4:</b><span class="blank"></span></div>
          <div class="answer"><b>5:</b><span class="blank"></span></div>
        </div>
        <div class="answer"><b>Comment:</b><span class="blank" style="margin-right:32px"></span></div>
      </div>
    </div>
  </div>
</section>

<section class="sheet sheet--two">
  <div class="checklist">
    <div class="row std"><div class="item">Conditional access Rules (no silly Rules, Geolocation filters in place for Sanctioned Countries)</div><div class="result"><div class="choices"><span><i></i>Yes</span><span><i></i>No</span></div><div class="answer"><b>Comment:</b><span class="blank"></span></div></div></div>
    <div class="row std"><div class="item">Review security access of all privileged access accounts</div><div class="result"><div class="choices"><span><i></i>Yes</span><span><i></i>No</span></div><div class="answer"><b>Comment:</b><span class="blank"></span></div></div></div>
    <div class="row std"><div class="item">Review Application Patching and confirm all workstations &amp; servers are up to date</div><div class="result"><div class="choices"><span><i></i>Yes</span><span><i></i>No</span></div><div class="answer"><b>Comment:</b><span class="blank"></span></div></div></div>
    <div class="row std"><div class="item">Review Fenestra Patching and confirm all workstations &amp; servers are up to date</div><div class="result"><div class="choices"><span><i></i>Yes</span><span><i></i>No</span></div><div class="answer"><b>Comment:</b><span class="blank"></span></div></div></div>
    <div class="row std"><div class="item">Review domain expiry dates</div><div class="result"><div class="choices"><span><i></i>Yes</span><span><i></i>No</span></div><div class="answer"><b>Comment:</b><span class="blank"></span></div></div></div>
    <div class="row std"><div class="item">Review certificate expiry dates (including internal services i.e. vHub)</div><div class="result"><div class="choices"><span><i></i>Yes</span><span><i></i>No</span></div><div class="answer"><b>Comment:</b><span class="blank"></span></div></div></div>
    <div class="row std"><div class="item">Confirm all devices are in Application Whitelisting enforcement mode</div><div class="result"><div class="choices"><span><i></i>Yes</span><span><i></i>No</span></div><div class="answer"><b>Comment:</b><span class="blank"></span></div></div></div>
    <div class="row std"><div class="item">Ensure DMARC, DKIM and SPF records are in place and up to date</div><div class="result"><div class="choices"><span><i></i>Yes</span><span><i></i>No</span></div><div class="answer"><b>Comment:</b><span class="blank"></span></div></div></div>
    <div class="row std"><div class="item">Confirm Retention Policies is configured and time specified</div><div class="result"><div class="choices"><span><i></i>Yes</span><span><i></i>No</span></div><div class="answer"><b>Comment:</b><span class="blank"></span></div></div></div>
    <div class="row std"><div class="item">Review Network Firewall Firmware is up to date and no ANY &lt;&gt; ANY rules in place</div><div class="result"><div class="choices"><span><i></i>Yes</span><span><i></i>No</span></div><div class="answer"><b>Comment:</b><span class="blank"></span></div></div></div>
    <div class="row std"><div class="item">Ensure critical network equipment is connected to UPS (min 20min run time)</div><div class="result"><div class="choices"><span><i></i>Yes</span><span><i></i>No</span></div><div class="answer"><b>Comment:</b><span class="blank"></span></div></div></div>
    <div class="row std"><div class="item">Ensure Access Layer Network device firmware is up to date (Switches &amp; Access Points)</div><div class="result"><div class="choices"><span><i></i>Yes</span><span><i></i>No</span></div><div class="answer"><b>Comment:</b><span class="blank"></span></div></div></div>
    <div class="row std"><div class="item">Ensure the latest backup configuration for managed network devices is current or automatically backed up monthly. Saved Network location must be secured</div><div class="result"><div class="choices"><span><i></i>Yes</span><span><i></i>No</span></div><div class="answer"><b>Comment:</b><span class="blank"></span></div></div></div>
    <div class="row std"><div class="item">Ensure MFP's &amp; Printers drivers up to date.<br>No Print Nightmare</div><div class="result"><div class="choices"><span><i></i>Yes</span><span><i></i>No</span></div><div class="answer"><b>Comment:</b><span class="blank"></span></div></div></div>
    <div class="row std"><div class="item">NAC Certificates are current (PEAP/EAP-TLS)</div><div class="result"><div class="choices"><span><i></i>Yes</span><span><i></i>No</span></div><div class="answer"><b>Comment:</b><span class="blank"></span></div></div></div>
    <div class="row std"><div class="item">Check DLP alerts and configuration</div><div class="result"><div class="choices"><span><i></i>Yes</span><span><i></i>No</span></div><div class="answer"><b>Comment:</b><span class="blank"></span></div></div></div>
  </div>
</section>

</body>
</html>
```